"Hushvale Chewlets" is the brand name for CBN infused Gummies for a restful sleep

Need a label for the glass jar and a round label for the lid. The gummy shapes are crescent white mons and blue stars or gummy sheep

You can use an 6 or 8 oz clear jar. Your illustration program should have this mock up.

Font styles to use
Sans Serif

```html
<!DOCTYPE html>
<html lang="en">
<head>
<meta charset="UTF-8">
<title>Hushvale Chewlets – Jar Label</title>
<link href="https://fonts.googleapis.com/css2?family=Montserrat:wght@600;700&family=Quicksand:wght@600;700&display=swap" rel="stylesheet">
<style>
  :root {
    --page: #f3f3f4;
    --navy: #1f2f68;
    --navy-deep: #15225a;
    --arc: #3d5596;
    --band: #2f4a94;
    --sky: #7cc6ee;
    --white: #ffffff;
    --moon: #f7d538;
  }
  * { margin: 0; padding: 0; box-sizing: border-box; }
  html, body {
    width: 1200px;
    height: 979px;
    overflow: hidden;
    background: var(--page);
  }
  .canvas {
    position: relative;
    width: 1200px;
    height: 979px;
    display: flex;
    align-items: center;
    justify-content: center;
  }
  .jar-label {
    position: relative;
    width: 760px;
    height: 720px;
    background: linear-gradient(180deg, var(--navy) 0%, var(--navy-deep) 100%);
    overflow: hidden;
    border-radius: 6px;
  }
  .label-arc {
    position: absolute;
    left: 50%;
    top: -250px;
    width: 760px;
    height: 760px;
    margin-left: -380px;
    border-radius: 50%;
    background: radial-gradient(circle at 50% 70%, var(--navy) 0%, var(--arc) 100%);
  }
  .night-scene {
    position: absolute;
    left: 50%;
    top: 70px;
    width: 390px;
    height: 215px;
    margin-left: -195px;
    border-radius: 110px;
    background: radial-gradient(ellipse at 55% 45%, rgba(247, 213, 56, 0.85) 0%, rgba(230, 232, 240, 0.55) 38%, rgba(61, 85, 150, 0) 72%);
  }
  .brand-name {
    position: absolute;
    left: 0;
    right: 0;
    top: 310px;
    font-family: "Montserrat", sans-serif;
    font-weight: 700;
    color: var(--sky);
    font-size: 78px;
    line-height: 1;
    letter-spacing: -1px;
  }
  .brand-name span { display: block; }
  .brand-name .line-one { padding-left: 150px; }
  .brand-name .line-two { padding-left: 310px; margin-top: 4px; }
  .product-type {
    position: absolute;
    left: 0;
    right: 0;
    top: 540px;
    text-align: center;
    font-family: "Montserrat", sans-serif;
    font-weight: 700;
    font-size: 34px;
    letter-spacing: 1px;
    color: var(--white);
  }
  .product-sub {
    position: absolute;
    left: 0;
    right: 0;
    top: 586px;
    text-align: center;
    font-family: "Quicksand", sans-serif;
    font-weight: 700;
    font-size: 30px;
    color: var(--sky);
  }
  .product-sub .small { font-size: 26px; font-weight: 600; }
  .info-band {
    position: absolute;
    left: 0;
    right: 0;
    top: 640px;
    height: 52px;
    background: var(--band);
    display: flex;
    align-items: center;
    justify-content: center;
    gap: 18px;
    font-family: "Montserrat", sans-serif;
    font-weight: 600;
    font-size: 22px;
    color: var(--white);
  }
</style>
</head>
<body>
  <main class="canvas">
    <section class="jar-label">
      <div class="label-arc"></div>
      <div class="night-scene" role="img" aria-label="Illustration of a yellow crescent moon among white clouds and small stars"></div>
      <h1 class="brand-name">
        <span class="line-one">Hushvale</span>
        <span class="line-two">Chewlets</span>
      </h1>
      <p class="product-type">CANNABIS-INFUSED</p>
      <p class="product-sub">Gummies <span class="small">with</span> CBN</p>
      <div class="info-band">
        <span>50 Gummies per Package</span>
        <span>|</span>
        <span>Net Wt. : 6 oz</span>
      </div>
    </section>
  </main>
</body>
</html>
```